LVT Company Overview and Framework Training Guide

I am creating a training guide that in intended to provide sales training to independent consultants. I am working on a new Company logo and would like to match the theme, but more importantly, I want to layout the content in a modern format that keeps users engaged. The sample logo is attached and I will add more blue before it's complete.

Target Market(s)

Technology sales reps and consultants

Industry/Entity Type

Information Technology

Font styles to use
Serif
Sans Serif

Colors
3176b5
0292cd
33a6d7
0355a3
ffffff
333333
606060
1b1b1b

Requirements
Must have
• I need a company overview and a few slides that define the problem my training will help solve. I also need to show the framework and sales process, along with a demo of the software platform.
Nice to have
• Video inserts would be helpful and some slide should allow me to build out steps of the workflow.

```html
<!DOCTYPE html>
<html lang="en">
<head>
<meta charset="utf-8">
<title>LVT New Opportunity Sales Guide</title>
<link href="https://fonts.googleapis.com/css2?family=Open+Sans:wght@400;600;700&display=swap" rel="stylesheet">
<style>
:root{
  --blue:#0355a3;
  --blue-mid:#1b6fc6;
  --blue-soft:#9fb4de;
  --navy:#0d4f96;
  --sky:#0292cd;
  --yellow:#fcc10e;
  --dark:#333333;
  --ink:#1b1b1b;
  --grey:#606060;
  --purple:#7030a0;
  --teal:#1a4f5e;
  --green:#4aa84a;
  --emerald:#14966a;
  --red:#e60000;
  --white:#ffffff;
  --page:#ffffff;
}
*{margin:0;padding:0;box-sizing:border-box}
html,body{width:1200px;height:1079px;overflow:hidden;background:var(--page)}
body{font-family:"Open Sans",Arial,sans-serif;color:var(--grey)}
.stage{position:absolute;left:0;top:0;width:1430px;height:1286px;transform:scale(.83916);transform-origin:0 0}
.slide{position:absolute;width:654px;height:368px;background:var(--white);overflow:hidden;box-shadow:0 1px 6px rgba(0,0,0,.18)}
.abs{position:absolute}
.badge{position:absolute;left:6px;top:5px;width:29px;height:29px;border-radius:50%;background:var(--blue);color:#fff;font-size:11px;display:flex;align-items:center;justify-content:center;box-shadow:0 0 0 2px #dfe8f3}
.side-label{position:absolute;transform:rotate(-90deg);transform-origin:left top;font-size:7px;letter-spacing:2.4px;color:#b3b3b3;white-space:nowrap}
.footer-url{position:absolute;font-size:6px;color:#888}

/* cover logo */
.brand{position:absolute;left:212px;top:135px;display:flex;align-items:center;gap:22px}
.brand-square{width:72px;height:72px;background:var(--blue)}
.brand-name{font-size:25px;font-weight:700;line-height:32px;color:#555;letter-spacing:.3px}

/* title slide */
.title-slide{background:var(--blue)}
.year{position:absolute;left:22px;top:125px;transform:rotate(-90deg);transform-origin:left top;color:#fff;font-size:40px;font-weight:400;letter-spacing:1px;line-height:44px}
.title-text{position:absolute;left:200px;top:138px;width:254px;text-align:center;color:#fff}
.title-text .pre{font-size:21px;line-height:26px}
.title-text .main{font-size:37px;line-height:44px}
.framework-tag{position:absolute;left:446px;top:344px;color:#fff;font-size:9.5px;letter-spacing:2px}

/* flow chart */
.node{position:absolute;border-radius:50%;display:flex;align-items:center;justify-content:center;text-align:center;font-size:9px;line-height:12px}
.tag{position:absolute;display:flex;align-items:center;justify-content:center;text-align:center;font-weight:700}
.step{position:absolute;top:177px;height:57px;background:#f0f0f0;border-radius:2px;box-shadow:0 1px 2px rgba(0,0,0,.25)}
.step-head{height:22px;color:#fff;font-size:9px;font-weight:700;display:flex;align-items:center;justify-content:center;border-radius:2px 2px 0 0}
.step-body{font-size:8.5px;font-weight:600;color:var(--ink);text-align:center;line-height:12px;padding-top:5px}
.chev-text{position:absolute;color:#fff;font-weight:700;text-align:center;font-size:11px;line-height:15px}

/* content slides */
.slide-title{position:absolute;font-size:22px;color:#555;font-weight:400}
.slide-title em{font-style:normal;color:var(--blue)}
.points{position:absolute;list-style:none;font-size:9.5px;color:#777}
.points li{height:33px}
.photo{position:absolute}

/* pain assessment */
.card{position:absolute;color:#fff;text-align:center;box-shadow:0 2px 3px rgba(0,0,0,.3)}
.card .kicker{font-size:10px;font-weight:600;margin-top:9px;letter-spacing:.3px}
.card .text{font-size:16px;font-weight:700;line-height:23px;margin-top:2px}
.card.deep{background:var(--navy)}
.card.mid{background:var(--blue-mid)}
.card.soft{background:var(--blue-soft)}
.dots{position:absolute;left:310px;top:48px;display:flex;gap:3px}
.dots span{width:4px;height:4px;border-radius:50%;background:var(--sky)}
</style>
</head>
<body>
<div class="stage">

  <!-- 1 Brand cover -->
  <section class="slide" style="left:48px;top:45px">
    <div class="brand">
      <div class="brand-square"></div>
      <div class="brand-name">LATERAL<br>VECTOR<br>TECHNOLOGIES</div>
    </div>
  </section>

  <!-- 2 Title -->
  <section class="slide title-slide" style="left:728px;top:45px">
    <div class="year">2018</div>
    <svg class="abs" style="left:0;top:0" width="654" height="368" viewBox="0 0 654 368">
      <circle cx="327" cy="185" r="174" fill="none" stroke="#fff" stroke-width="1"/>
      <circle cx="327" cy="185" r="145" fill="none" stroke="#fff" stroke-width="46"/>
      <circle cx="577" cy="40" r="51" fill="#fff"/>
      <circle cx="547" cy="135" r="27" fill="#fff"/>
      <circle cx="474" cy="30" r="9.5" fill="#fff"/>
    </svg>
    <div class="title-text">
      <div class="pre">New Opportunity</div>
      <div class="main">Sales Guide</div>
    </div>
    <div class="framework-tag">LVT Consulting Framework</div>
  </section>

  <!-- 3 Sales process -->
  <section class="slide" style="left:48px;top:459px">
    <div class="badge">3</div>
    <svg class="abs" style="left:0;top:0" width="654" height="368" viewBox="0 0 654 368">
      <defs>
        <marker id="arrow" viewBox="0 0 6 6" refX="5" refY="3" markerWidth="5" markerHeight="5" orient="auto">
          <path d="M0 0 L6 3 L0 6 z" fill="#2f78c4"/>
        </marker>
      </defs>
      <g stroke="#2f78c4" stroke-width="1" fill="none" marker-end="url(#arrow)">
        <line x1="120" y1="56" x2="144" y2="56"/>
        <line x1="242" y1="56" x2="266" y2="56"/>
        <line x1="366" y1="56" x2="390" y2="56"/>
        <line x1="516" y1="38" x2="538" y2="27"/>
        <line x1="571" y1="46" x2="571" y2="66"/>
        <line x1="400" y1="88" x2="378" y2="104"/>
        <line x1="328" y1="127" x2="278" y2="127"/>
        <line x1="128" y1="136" x2="76" y2="158"/>
        <line x1="110" y1="205" x2="138" y2="205"/>
        <line x1="245" y1="205" x2="272" y2="205"/>
        <line x1="393" y1="205" x2="419" y2="205"/>
        <line x1="521" y1="205" x2="538" y2="205"/>
        <polyline points="609,242 609,260 33,260 33,280"/>
      </g>
      <polygon points="452,6 494,30 494,79 452,103 410,79 410,30" fill="var(--purple)"/>
      <polygon points="14,286 134,286 154,319 134,352 14,352 24,319" fill="var(--blue)"/>
      <polygon points="132,286 305,286 330,319 305,352 132,352 152,319" fill="var(--yellow)"/>
      <polygon points="296,286 505,286 530,319 505,352 296,352 321,319" fill="var(--dark)"/>
    </svg>
    <div class="node" style="left:32px;top:16px;width:76px;height:76px;background:var(--blue);color:#fff">New<br>opportunity<br>Generated</div>
    <div class="node" style="left:154px;top:16px;width:76px;height:76px;background:var(--yellow);color:var(--ink)">Discovery<br>Call/<br>Meeting</div>
    <div class="node" style="left:278px;top:16px;width:78px;height:78px;background:var(--dark);color:#fff">Pain<br>Assessment<br>/ Challenges</div>
    <div class="abs" style="left:408px;top:31px;width:88px;text-align:center;color:#fff;font-size:8.5px;line-height:12px">Agreed to problem potential solution and process to get to a decision (Yes/No)</div>
    <div class="tag" style="left:548px;top:12px;width:45px;height:25px;background:var(--red);color:#fff;font-size:14px">NO</div>
    <div class="tag" style="left:520px;top:70px;width:121px;height:50px;background:var(--teal);color:#fff;font-weight:400;font-size:10px;line-height:14px;border-radius:3px">Discuss what needs to happen to get there or agreed that it's a no</div>
    <div class="tag" style="left:142px;top:114px;width:128px;height:25px;background:var(--blue);color:#fff;font-size:10.5px">Research &amp; analysis</div>
    <div class="tag" style="left:332px;top:114px;width:44px;height:25px;background:var(--green);color:#fff;font-size:13px">yes</div>

    <div class="step" style="left:10px;width:98px"><div class="step-head" style="background:var(--purple)">Provider Matrix</div><div class="step-body">Rakings, scores,<br>Alignment</div></div>
    <div class="step" style="left:140px;width:103px"><div class="step-head" style="background:var(--yellow);color:var(--ink)">Channel Reviews</div><div class="step-body">Provider Reviews Case<br>Studies References</div></div>
    <div class="step" style="left:274px;width:117px"><div class="step-head" style="background:var(--emerald)">Road map</div><div class="step-body">Technical SOW POC/Pilot<br>Provider Meetings</div></div>
    <div class="step" style="left:421px;width:98px"><div class="step-head" style="background:var(--blue)">Short List</div><div class="step-body">Evaluations, Demos<br>Customer Meetings</div></div>
    <div class="step" style="left:540px;width:102px"><div class="step-head" style="background:var(--green)">Financial Analysis</div><div class="step-body">Savings, TCO<br>Forecast Budgets</div></div>

    <div class="chev-text" style="left:26px;top:304px;width:100px;font-size:12px">Proposal<br>Generation</div>
    <div class="chev-text" style="left:164px;top:290px;width:140px;color:var(--ink)">Fulfillment<br>Presentations<br>Criteria Alignment<br>Decision Making</div>
    <div class="chev-text" style="left:330px;top:290px;width:166px">On going Engagement<br>TEM, MACD<br>insights<br>Future Projects</div>
  </section>

  <!-- 4 Appointment -->
  <section class="slide" style="left:728px;top:459px">
    <div class="badge">4</div>
    <h2 class="slide-title" style="left:61px;top:30px">You have an <em>Appointment</em></h2>
    <ul class="points" style="left:39px;top:111px">
      <li>What's the purpose? UFC</li>
      <li>Goals &amp; Objectives</li>
      <li>Who is the meeting with and where?</li>
      <li>What are typical pains or issues we have solved that are similar?</li>
      <li>How to prepare? First meeting requires</li>
      <li>mostly listening skills</li>
    </ul>
    <div class="side-label" style="left:7px;top:328px">LVT Consulting Framework</div>
    <div class="photo" role="img" aria-label="Photo strips of two people shaking hands" style="left:365px;top:0;width:289px;height:368px;clip-path:polygon(35px 0,100% 0,100% 100%,35px 100%,0 50%);background:linear-gradient(100deg,#9a5a2e 0%,#c8895a 35%,#7a4a2e 60%,#6c7f9a 80%,#3e5678 100%)"></div>
    <div class="footer-url" style="left:6px;top:353px">www.lvtguide.net</div>
  </section>

  <!-- 5 Discovery Call -->
  <section class="slide" style="left:48px;top:873px">
    <div class="photo" role="img" aria-label="Photo of a businessman in a suit giving a thumbs up" style="left:0;top:0;width:446px;height:369px;clip-path:polygon(0 0,150px 0,446px 369px,0 369px);background:linear-gradient(120deg,#1d2738 0%,#2f4263 35%,#c48c6c 60%,#3a4f78 85%,#1d2738 100%)"></div>
    <div class="badge">5</div>
    <h2 class="slide-title" style="right:44px;top:38px;text-align:right"><em>Discovery</em> Call</h2>
    <ul class="points" style="right:44px;top:117px;text-align:right">
      <li>Introductions</li>
      <li>Understanding why they need help ( Why use a partner? )</li>
      <li>What's the problem? Pain discovery</li>
      <li>Success criteria</li>
      <li>Timeline/Roadmap</li>
    </ul>
    <div class="side-label" style="left:640px;top:310px">LVT Consulting Framework</div>
    <div class="footer-url" style="right:16px;top:349px">www.lvtguide.net</div>
  </section>

  <!-- 6 Pain Assessment -->
  <section class="slide" style="left:728px;top:873px">
    <div class="badge">6</div>
    <h2 class="slide-title" style="left:0;width:664px;top:6px;text-align:center;color:var(--blue)">Pain Assessment/Challenges</h2>
    <div class="dots"><span></span><span></span><span></span><span style="background:#33a6d7"></span><span style="background:#4cc08a"></span></div>
    <div class="card deep" style="left:46px;top:91px;width:174px;height:81px"><div class="kicker">AGREE ON</div><div class="text">Agree on this issues<br>and priorities</div></div>
    <div class="card mid" style="left:239px;top:91px;width:174px;height:81px"><div class="kicker">DISCUSS</div><div class="text">Discuss potential<br>solutions</div></div>
    <div class="card soft" style="left:430px;top:91px;width:177px;height:81px"><div class="kicker">AGREE ON</div><div class="text">Agree on best<br>direction/strategy</div></div>
    <div class="card deep" style="left:145px;top:220px;width:174px;height:98px"><div class="kicker">DISCUSS</div><div class="text">Discuss how to<br>present the solution<br>with client</div></div>
    <div class="card mid" style="left:338px;top:220px;width:174px;height:98px"><div class="kicker">ROADMAP</div><div class="text">Develop Roadmap<br>and decision<br>criteria</div></div>
    <div class="side-label" style="left:9px;top:340px">LVT Consulting Framework</div>
    <div class="footer-url" style="left:6px;top:353px">www.lvtguide.net</div>
  </section>

</div>
</body>
</html>
```